Brookvale Services telephone book advert

Design a tellwick directory telephone book advertisement. Attached is a current version of the brookvale services advert. Please use the same information as detailed on the existing advert but arty!. Overall size should be 130 mm by 91 mm portrait using one of the specified colours plus black. Any background should be opaque (not white). and delivered in the formats as specified.

```html
<!DOCTYPE html>
<html lang="en">
<head>
<meta charset="utf-8">
<title>Brookvale Services Limited – Directory Advert</title>
<link href="https://fonts.googleapis.com/css2?family=Source+Sans+3:wght@300;400;600;700&display=swap" rel="stylesheet">
<style>
  :root {
    --navy: #0f4a87;
    --cream: #f4e9bc;
    --ink: #111111;
  }
  * { margin: 0; padding: 0; box-sizing: border-box; }
  html, body { width: 840px; height: 1200px; overflow: hidden; background: var(--navy); }
  body { font-family: "Source Sans 3", "Myriad Pro", sans-serif; }
  .advert { position: relative; width: 840px; height: 1200px; background: var(--navy); color: var(--cream); }
  .line { position: absolute; left: 0; width: 100%; text-align: center; white-space: nowrap; line-height: 1; }

  .brand-name { font-weight: 700; font-size: 84px; letter-spacing: -1px; }
  .brand-name.first { top: 44px; }
  .brand-name.second { top: 112px; }
  .brand-suffix { top: 198px; font-weight: 300; font-size: 50px; letter-spacing: 30px; padding-left: 30px; }

  .info-panel { position: absolute; left: 13px; top: 293px; width: 814px; height: 643px; background: var(--cream); color: var(--ink); }
  .info-panel .line { width: 814px; }
  .panel-title { top: 24px; font-weight: 600; font-size: 46px; }
  .service { position: absolute; left: 25px; font-size: 32px; line-height: 42px; width: 780px; }
  .service b { font-weight: 700; }
  .service.emergencies { top: 81px; left: 25px; }
  .service.maintenance { top: 147px; left: 27px; }
  .service.rehabilitation { top: 211px; left: 27px; }
  .service.survey { top: 309px; left: 24px; }

  .contact-role { top: 380px; color: var(--navy); font-weight: 600; font-size: 35px; }
  .contact-name { top: 404px; color: var(--navy); font-weight: 700; font-size: 68px; }
  .contact-email { top: 467px; color: var(--navy); font-size: 30px; }
  .web-intro { top: 530px; font-size: 36px; }
  .web-address { top: 565px; color: var(--navy); font-weight: 700; font-size: 52px; }

  .call-prompt { top: 958px; font-weight: 600; font-size: 32px; padding-left: 6px; }
  .phone { position: absolute; top: 1000px; left: 70px; display: flex; align-items: center; gap: 20px; }
  .phone-icon { width: 90px; height: 96px; fill: var(--cream); }
  .phone-number { font-weight: 700; font-size: 132px; line-height: 1; letter-spacing: -1px; }
  .address { top: 1142px; font-size: 30px; }
</style>
</head>
<body>
<main class="advert">
  <div class="line brand-name first">BROOKVALE</div>
  <div class="line brand-name second">SERVICES</div>
  <div class="line brand-suffix">LIMITED</div>

  <section class="info-panel">
    <h1 class="line panel-title">Home Buyer Surveys</h1>
    <p class="service emergencies"><b>Emergencies:</b> Unblocking &amp; high pressure cleaning</p>
    <p class="service maintenance"><b>Maintenance:</b> Jetting, de-scaling &amp; root cutting</p>
    <p class="service rehabilitation"><b>Rehabilitation:</b> Structural re-lining of damaged and leaky drains</p>
    <p class="service survey"><b>Survey:</b> Modern CCTV, condition reports</p>

    <div class="line contact-role">Contracts Manager</div>
    <div class="line contact-name">OWEN MARCHANT</div>
    <div class="line contact-email">office@bvs.gg</div>
    <div class="line web-intro">For more information please visit our website:</div>
    <div class="line web-address">www.bvs.gg</div>
  </section>

  <div class="line call-prompt">For local drainage expertise, call</div>
  <div class="phone">
    <svg class="phone-icon" viewBox="0 0 24 24" aria-hidden="true">
      <path d="M6.6 2.2c.6-.4 1.4-.3 1.8.3l2.2 3.3c.4.6.3 1.3-.2 1.8L8.9 9c1.2 2.6 3.5 4.9 6.1 6.1l1.4-1.5c.5-.5 1.2-.6 1.8-.2l3.3 2.2c.6.4.7 1.2.3 1.8l-1.5 2.3c-.6.9-1.7 1.3-2.7 1C10.6 18.9 5.1 13.4 3.3 6.4c-.3-1 .1-2.1 1-2.7z"/>
    </svg>
    <span class="phone-number">318-640</span>
  </div>
  <div class="line address">Les Banques Lane, St Andrew, Guernsey GY6 8QT</div>
</main>
</body>
</html>
```